Calloway Pipeworks Summary ESG brochure report

We are looking to create a summary ESG report for and Oil and Gas Midstream producer - Calloway Pipeworks. This is a report on their environmental, social and governance (ESG) aspects as well as a summary of who they are. It's focused on Wyoming oil and gas midstream for pipeline transport of oil and gas. We are to emphasize their environmental aspects, social aspects with visuals, graphics, etc. Attached is a example ESG report that is larger than what we want, but gives the designer of what an ESG report is.
The attached Harrowgate 2019 report is an "IDEA of what we are looking for - but on a smaller scale. This is a much larger report, but expands on the idea of what we are trying to do.
Client is:
https://www.callowaypipeworks.example/
The outline brochure documens is what we have written and given examples of graphics with our writing / bullets of what we have visioned through the brochure. We are looking for a document with these items and graphs in it.
We have attached a few excel sheets and creations to hopefully better visualize our ideas and timelines to assist the graphic designers.
Look and feel
Each slider illustrates characteristics of the customer's brand and the style your logo design should communicate.

```html
<!DOCTYPE html>
<html lang="en">
<head>
<meta charset="utf-8">
<title>Calloway Pipeworks ESG Summary Brochure</title>
<link href="https://fonts.googleapis.com/css2?family=Barlow:wght@400;500;600;700;800&display=swap" rel="stylesheet">
<style>
:root{
  --bg:#d6d6d6;
  --paper:#ffffff;
  --brown:#6a3d1c;
  --brown-dark:#4a2a12;
  --gold:#b57d3f;
  --tan:#d9b98f;
  --ink:#2b2b2b;
  --grey:#8a8a8a;
  --night:#1c1410;
}
*{margin:0;padding:0;box-sizing:border-box}
html,body{width:684px;height:1200px;overflow:hidden}
body{background:var(--bg);font-family:"Barlow",Arial,sans-serif;color:var(--ink);position:relative}
.page{position:absolute;width:298px;height:384px;background:var(--paper);overflow:hidden;box-shadow:0 2px 6px rgba(0,0,0,.25)}
.p1{left:30px;top:8px}.p2{left:350px;top:8px}
.p3{left:30px;top:410px}.p4{left:350px;top:410px}
.p5{left:30px;top:808px}.p6{left:350px;top:808px}
.frame{position:absolute;inset:0;width:100%;height:100%}
.brand{position:absolute;top:22px;left:0;right:0;display:flex;justify-content:center;align-items:center;gap:6px;font-weight:700;font-size:13px;letter-spacing:.5px;text-transform:uppercase}
.brand .mark{width:9px;height:9px;background:var(--gold)}
.photo{position:absolute}
.cover-photo{inset:0;background:linear-gradient(180deg,#0f0c0b 0%,#3a1a0c 40%,#c2501a 62%,#f2a33a 72%,#2a130a 88%,#0d0907 100%)}
.rig-photo{inset:0;background:linear-gradient(180deg,#c9d3dd 0%,#e8dccd 38%,#f0b06a 55%,#8a6a58 72%,#2d4a63 100%)}
.cover-brand{color:#fff}
.rig-brand{color:var(--brown)}
.cover-contact{position:absolute;left:18px;bottom:26px;color:#ddd;font-size:5px;line-height:1.6}
.body{font-size:4.4px;line-height:1.55;color:#555;text-align:justify}
.h2{font-weight:700;color:var(--brown);font-size:12px;line-height:1.15}
.h3{font-weight:700;color:var(--brown);font-size:10px}
/* page 3 */
.ceo-photo{left:22px;top:60px;width:64px;height:78px;background:linear-gradient(180deg,#cfd4d8,#8e969c)}
.ceo-title{position:absolute;left:94px;top:60px;font-size:5px;font-weight:700;color:var(--brown);line-height:1.3}
.letter{position:absolute;left:94px;top:74px;right:22px}
.letter-full{position:absolute;left:22px;top:146px;right:22px}
.letter p,.letter-full p{margin-bottom:4px}
.sign{position:absolute;right:24px;top:300px;text-align:right;font-size:6px;font-weight:700;color:var(--ink)}
.sign span{display:block;font-weight:400;font-size:4.5px;color:var(--grey)}
/* page 4 */
.p4 .h2{position:absolute;left:26px;top:58px;right:30px}
.tabs{position:absolute;left:26px;top:92px;display:flex;gap:8px;font-size:5.5px;font-weight:600}
.tabs span{display:flex;align-items:center;gap:3px}
.tabs i{width:7px;height:7px;background:var(--brown);display:inline-block}
.tech-photo{left:26px;top:106px;width:246px;height:86px;background:linear-gradient(135deg,#0b2a4a,#1f5f95 55%,#0c223c)}
.p4 .h3{position:absolute;left:26px;top:202px}
.p4 .story{position:absolute;left:26px;top:218px;right:26px}
/* page 5 */
.p5 .h3.a{position:absolute;left:24px;top:54px}
.p5 .story{position:absolute;left:24px;top:68px;right:24px}
.p5 .h3.b{position:absolute;left:24px;top:108px}
.bullets{position:absolute;left:24px;top:124px;right:24px;list-style:none;font-size:5px;color:#444}
.bullets li{display:flex;align-items:center;gap:4px;margin-bottom:4px}
.bullets li::before{content:"";width:5px;height:5px;background:var(--brown);flex:none}
.strategy{position:absolute;left:22px;right:22px;top:226px;height:124px;background:var(--brown);padding:10px}
.strategy .title{color:#fff;font-weight:700;font-size:10px}
.pillars{display:flex;justify-content:space-around;margin-top:12px}
.pillar{display:flex;flex-direction:column;align-items:center;gap:6px;color:#f0e2cf;font-size:5.5px;font-weight:600}
.pillar b{width:36px;height:36px;border-radius:50%;background:#fff;display:block}
/* page 6 */
.p6 .h2{position:absolute;left:26px;top:58px;right:30px}
.rows{position:absolute;left:24px;right:24px;top:100px}
.row{display:flex;align-items:center;gap:10px;height:30px;margin-bottom:5px;background:var(--brown);padding:0 10px;color:#f3e6d3;font-size:5.5px}
.row svg{flex:none}
.diagram{position:absolute;left:24px;top:272px;width:130px;height:96px}
.legend{position:absolute;left:164px;top:286px;list-style:none;font-size:5px;color:#444}
.legend li{display:flex;align-items:center;gap:4px;margin-bottom:5px}
.legend li::before{content:"";width:4px;height:4px;border-radius:50%;background:var(--gold)}
</style>
</head>
<body>

<!-- Cover -->
<section class="page p1">
  <div class="photo cover-photo" role="img" aria-label="Oil pump jack silhouetted against an orange sunset sky"></div>
  <div class="brand cover-brand"><span class="mark"></span>Calloway Pipeworks</div>
  <div class="cover-contact">
    1200 Example Avenue, Suite 400<br>Denver, Colorado 80202<br>555-0142<br>https://www.callowaypipeworks.example/
  </div>
</section>

<!-- Back / intro cover -->
<section class="page p2">
  <div class="photo rig-photo" role="img" aria-label="Offshore drilling platform at sunrise over the sea"></div>
  <div class="brand rig-brand"><span class="mark"></span>Calloway Pipeworks</div>
</section>

<!-- CEO message -->
<section class="page p3">
  <svg class="frame" viewBox="0 0 298 384" preserveAspectRatio="none" aria-hidden="true">
    <polygon points="0,0 70,0 0,40" fill="var(--brown)"/>
    <polygon points="228,0 298,0 298,40" fill="var(--brown)"/>
    <polygon points="0,0 298,0 298,14 0,14" fill="var(--brown-dark)"/>
    <polygon points="0,384 0,344 90,384" fill="var(--tan)"/>
    <polygon points="298,384 298,344 208,384" fill="var(--tan)"/>
  </svg>
  <div class="photo ceo-photo" role="img" aria-label="Portrait of the chief executive officer"></div>
  <div class="ceo-title">Who We Are<br>Message from our CEO</div>
  <div class="letter body">
    <p>Our team moves energy across the Rockies with care for the land, the people who live on it, and the communities that depend on safe, reliable and responsible pipeline service every day.</p>
    <p>This summary shares how we measure our footprint, invest in our workforce and govern our business so that each decision builds lasting value for owners, neighbors and partners.</p>
  </div>
  <div class="letter-full body">
    <p>Our team moves energy across the Rockies with care for the land, the people who live on it, and the communities that depend on safe, reliable and responsible pipeline service every day.</p>
    <p>This summary shares how we measure our footprint, invest in our workforce and govern our business so that each decision builds lasting value for owners, neighbors and partners.</p>
  </div>
  <div class="sign">Daniel P Whitcombe<span>Chief Executive Officer &amp; President</span></div>
</section>

<!-- Story -->
<section class="page p4">
  <svg class="frame" viewBox="0 0 298 384" preserveAspectRatio="none" aria-hidden="true">
    <polygon points="0,0 298,0 298,14 0,14" fill="var(--brown-dark)"/>
    <polygon points="0,0 70,0 0,40" fill="var(--brown)"/>
    <polygon points="228,0 298,0 298,40" fill="var(--brown)"/>
    <polygon points="0,384 0,344 90,384" fill="var(--tan)"/>
    <polygon points="298,384 298,344 208,384" fill="var(--tan)"/>
  </svg>
  <div class="h2">Stewarding a sustainable path to stakeholder value in the Rockies</div>
  <div class="tabs"><span><i></i>Story</span><span><i></i>Strategy</span><span><i></i>Principles / Values</span></div>
  <div class="photo tech-photo" role="img" aria-label="Hand touching a glowing digital industry network interface"></div>
  <div class="h3">The Calloway Pipeworks Story</div>
  <div class="story body">
    <p>This summary shares how we measure our footprint, invest in our workforce and govern our business so that each decision builds lasting value for owners, neighbors and partners. Our team moves energy across the Rockies with care for the land, the people who live on it, and the communities that depend on safe, reliable and responsible pipeline service every day.</p>
  </div>
</section>

<!-- Strategy -->
<section class="page p5">
  <svg class="frame" viewBox="0 0 298 384" preserveAspectRatio="none" aria-hidden="true">
    <polygon points="0,0 298,0 298,14 0,14" fill="var(--brown-dark)"/>
    <polygon points="0,0 70,0 0,40" fill="var(--brown)"/>
    <polygon points="228,0 298,0 298,40" fill="var(--brown)"/>
    <polygon points="0,384 0,344 90,384" fill="var(--tan)"/>
    <polygon points="298,384 298,344 208,384" fill="var(--tan)"/>
  </svg>
  <div class="h3 a">The Calloway Pipeworks Story</div>
  <div class="story body"><p>Our team moves energy across the Rockies with care for the land, the people who live on it, and the communities that depend on safe, reliable and responsible pipeline service every day.</p></div>
  <div class="h3 b">Our Sustainability Strategy</div>
  <ul class="bullets">
    <li>Reduce methane intensity across gathering assets</li>
    <li>Protect water and wildlife near our routes</li>
    <li>Support safety training for every field crew</li>
    <li>Partner with local Wyoming communities</li>
    <li>Report progress with clear annual metrics</li>
    <li>Keep strong board oversight of risk</li>
  </ul>
  <div class="strategy">
    <div class="title">Our Strategy</div>
    <div class="pillars">
      <div class="pillar"><b></b>Environment</div>
      <div class="pillar"><b></b>Social</div>
      <div class="pillar"><b></b>Governance</div>
    </div>
  </div>
</section>

<!-- Principles -->
<section class="page p6">
  <svg class="frame" viewBox="0 0 298 384" preserveAspectRatio="none" aria-hidden="true">
    <polygon points="0,0 298,0 298,14 0,14" fill="var(--brown-dark)"/>
    <polygon points="0,0 70,0 0,40" fill="var(--brown)"/>
    <polygon points="228,0 298,0 298,40" fill="var(--brown)"/>
    <polygon points="0,384 0,344 90,384" fill="var(--tan)"/>
    <polygon points="298,384 298,344 208,384" fill="var(--tan)"/>
  </svg>
  <div class="h2">Stewarding a sustainable path to stakeholder value in the Rockies</div>
  <div class="rows">
    <div class="row"><svg width="16" height="16" viewBox="0 0 16 16"><circle cx="8" cy="8" r="6" fill="none" stroke="var(--tan)" stroke-width="1.4"/><path d="M5 8l2 2 4-4" fill="none" stroke="var(--tan)" stroke-width="1.4"/></svg>Lower emissions through leak detection</div>
    <div class="row"><svg width="16" height="16" viewBox="0 0 16 16"><path d="M8 2c-3 3-4 6-2 9 1 1 3 1 4 0 2-3 1-6-2-9z" fill="none" stroke="var(--tan)" stroke-width="1.4"/></svg>Restore land after every construction project</div>
    <div class="row"><svg width="16" height="16" viewBox="0 0 16 16"><circle cx="8" cy="5" r="2.5" fill="none" stroke="var(--tan)" stroke-width="1.4"/><path d="M3 14c0-3 2-5 5-5s5 2 5 5" fill="none" stroke="var(--tan)" stroke-width="1.4"/></svg>Invest in safety and local hiring</div>
    <div class="row"><svg width="16" height="16" viewBox="0 0 16 16"><path d="M2 6h12L8 2zM3 7v6M8 7v6M13 7v6M2 14h12" fill="none" stroke="var(--tan)" stroke-width="1.3"/></svg>Ethical oversight from an independent board</div>
  </div>
  <svg class="diagram" viewBox="0 0 130 96" aria-label="Stewardship diagram">
    <line x1="65" y1="50" x2="28" y2="20" stroke="var(--gold)"/>
    <line x1="65" y1="50" x2="102" y2="20" stroke="var(--gold)"/>
    <line x1="65" y1="50" x2="65" y2="84" stroke="var(--gold)"/>
    <circle cx="28" cy="20" r="14" fill="var(--gold)"/>
    <circle cx="102" cy="20" r="14" fill="var(--gold)"/>
    <circle cx="65" cy="84" r="11" fill="var(--gold)"/>
    <circle cx="65" cy="50" r="17" fill="var(--brown)"/>
    <g font-family="Barlow, Arial, sans-serif" font-size="6" fill="#fff" text-anchor="middle" font-weight="600">
      <text x="65" y="52">Stewards</text>
      <text x="28" y="22">Land</text>
      <text x="102" y="22">People</text>
      <text x="65" y="86">Trust</text>
    </g>
  </svg>
  <ul class="legend">
    <li>Environment stewardship</li>
    <li>Safety culture</li>
    <li>Community partners</li>
    <li>Governance</li>
    <li>Transparency</li>
  </ul>
</section>

</body>
</html>
```